Business Performance Improvement Book Cover Design Project

We need a book cover design for a new company, based in Eastern Australia, called Marrowby Global. We advise clients on process improvement, continuous improvement and business performance improvement, especially in the manufacturing areas and Fast Moving Consumer Goods industries.
We have a written a book designed to demonstrate our very high calibre of knowledge and to use as a marketing tool for prospective clients. We hope to give it out at training seminars and as a comprehensive business card.

Title of the book is: A holistic approach to Business Performance Improvement.
Subtitle: Tailor a Continuous Improvement approach to suit your company culture.
Author: by Gordon Marrowby
Back Cover: No need for a bar code in this edition. An important aspect is that we will distribute by hand. Text below for back page.

'For the experienced Business Performers, this book is designed to offer an insight into the advantages and an example of an approach to Business Improvement. It is not the only way but it is tried and tested in world class companies and it works. For those new to Continuous Improvement, it offers a helpful introduction to a holistic business improvement system, an overview of important success factors and pitfalls, recommendations on how to implement tools and methods and a quick guide to see when to use which tools. '

'Consultancies are one of many tools management teams can engage and management must make sure the consultants tailor their approach to suit its business needs and culture and not vice versa.'

End of text for back cover.

Business Performance Improvement is also known as or can include:
Continuous Improvement
Process Improvement
Lean Six Sigma
Operational Excellence
Total Productive Maintenance
Hadeko Assembly Method
Total Quality Management
Business Process Re engineering
Output Ladder
=
Marrowby Global

The book size is 175 x 240 mm and will need a 10-15mm bleed. The spine is not known at this stage exactly and will need to be updated once the printing is finished but I suggest a 10mm until I have the exact size.

Our company colours are Pantone 288, R0,G75,B141, C100,M79,Y17,K3. Attached are some other publications that give a sense of what we like to portray, Some words which might add to this are: professional, elegance, quality, sleek.
Updates

Reason: After receiving the designs, I realised that I needed to update the brief with more and better quality information for designers to work with.

Target Market(s)

people in the accounting and insolvency industries, production managers and CEOs, Chief Operating Officers, members of the executive team of large companies and GMs of small companies.

Industry/Entity Type

Marketing

Requirements
Must have
• Communicate an image that shows an improvement or increase of something.
Very professional and elegant
Emphasis on the words 'Business Performance Improvement' in the title, subtitle also important
Must appeal to a high-end of the market audience
Nice to have
• Recommendation for your cover to be gloss or matt in print
Image can be indirectly related to money but not specifically
Somehow that it matches or is not so different to the attached brochure
Should not have
• Not be too loud or commercial
Book jacket. WIll be printed as soft cover first run and hard cover 2nd run

```html
<!DOCTYPE html>
<html lang="en">
<head>
<meta charset="utf-8">
<title>A Holistic Approach To Business Performance Improvement</title>
<link rel="stylesheet" href="https://fonts.googleapis.com/css2?family=Noto+Serif:wdth,wght@62.5..100,400&display=swap">
<style>
  :root {
    --paper: #ffffff;
    --ink: #000000;
    --brand-blue: #3e6896;
    --brand-blue-deep: #2f5682;
    --brand-blue-soft: #5c82ad;
    --glow: #b9c8f0;
    --shadow: rgba(0, 0, 0, 0.55);
  }
  html, body {
    margin: 0;
    padding: 0;
    overflow: hidden;
    background: var(--paper);
  }
  .cover {
    position: relative;
    width: 846px;
    height: 1200px;
    overflow: hidden;
    background: var(--paper);
    font-family: "Noto Serif", "DejaVu Serif", serif;
    font-stretch: 70%;
    color: var(--ink);
  }
  .cover-art {
    position: absolute;
    left: 0;
    top: 0;
    width: 846px;
    height: 1200px;
  }
  .title {
    position: absolute;
    right: 43px;
    top: 52px;
    margin: 0;
    text-align: right;
    font-weight: 400;
    font-size: 80px;
    line-height: 108px;
    letter-spacing: -0.5px;
    text-shadow: 4px 4px 4px var(--shadow);
  }
  .title span { display: block; }
  .subtitle {
    position: absolute;
    right: 48px;
    top: 592px;
    width: 560px;
    margin: 0;
    text-align: right;
    font-size: 37px;
    line-height: 51px;
    text-shadow: 3px 3px 3px var(--shadow);
  }
  .author {
    position: absolute;
    right: 50px;
    top: 805px;
    margin: 0;
    font-size: 33px;
    line-height: 44px;
    white-space: nowrap;
    text-shadow: 3px 3px 3px var(--shadow);
  }
</style>
</head>
<body>
<main class="cover">
  <svg class="cover-art" width="846" height="1200" viewBox="0 0 846 1200" xmlns="http://www.w3.org/2000/svg">
    <defs>
      <linearGradient id="ornament-tone" x1="0" y1="0" x2="1" y2="1">
        <stop offset="0" stop-color="#5c82ad"/>
        <stop offset="0.6" stop-color="#3e6896" stop-opacity="0.55"/>
        <stop offset="1" stop-color="#3e6896" stop-opacity="0"/>
      </linearGradient>
      <linearGradient id="ornament-tone-low" x1="0" y1="1" x2="1" y2="0">
        <stop offset="0" stop-color="#5c82ad"/>
        <stop offset="0.6" stop-color="#3e6896" stop-opacity="0.55"/>
        <stop offset="1" stop-color="#3e6896" stop-opacity="0"/>
      </linearGradient>
      <linearGradient id="arrow-fill" x1="0" y1="0" x2="1" y2="0">
        <stop offset="0" stop-color="#2f5682"/>
        <stop offset="1" stop-color="#3a6290"/>
      </linearGradient>
      <filter id="arrow-glow" x="-20%" y="-20%" width="140%" height="140%">
        <feDropShadow dx="3" dy="0" stdDeviation="4" flood-color="#b9c8f0" flood-opacity="0.9"/>
      </filter>
    </defs>
    <rect class="ornament ornament-top" role="img" aria-label="Blue embossed floral scroll ornament along the top left" x="0" y="0" width="380" height="300" fill="url(#ornament-tone)"/>
    <rect class="ornament ornament-bottom" role="img" aria-label="Blue embossed floral leaf ornament along the bottom left" x="0" y="820" width="330" height="380" fill="url(#ornament-tone-low)"/>
    <polygon class="rising-arrow" points="0,150 18,152 325,595 0,1040" fill="url(#arrow-fill)" filter="url(#arrow-glow)"/>
  </svg>

  <h1 class="title">
    <span>A Holistic</span>
    <span>Approach</span>
    <span>To Business</span>
    <span>Performance</span>
    <span>Improvement</span>
  </h1>

  <p class="subtitle">Tailor a<br>Continuous Improvement<br>approach to suit your company<br>culture.</p>

  <p class="author">Gordon Marrowby B. Mech Eng., M. Sc (VRK)</p>
</main>
</body>
</html>
```